Vision Mission Values Layout for Displaying

We our looking for a format or template that we can transfer onto canvas, metal, or picture to display in our front lobby, break room, and conference room. We would like to incorporate our company logo and colors. Red Black & White. We would like them all displayed on the same canvas, sheet metal, or picture. This is our first time using this site we are hoping to use this site for our web design and possible re design our logo. When we walk into other businesses we see their vision, mission, and values displayed. We are looking for something similar.

Industry/Entity Type

It Company

Requirements
Must have
• Company Name and Logo
• Mission Vision and Values
Nice to have
• the definitions
Should not have
• Contact Information

```html
<!DOCTYPE html>
<html lang="en">
<head>
<meta charset="utf-8">
<title>Harlow Steelworks – Mission, Vision &amp; Values</title>
<link rel="stylesheet" href="https://fonts.googleapis.com/css2?family=Oswald:wght@500;700&family=Archivo+Narrow:wght@400&display=swap">
<style>
  :root {
    --paper: #ffffff;
    --ink: #231f20;
    --brand-red: #ec3a33;
    --panel-black: #000000;
    --value-gold: #f4dba9;
    --white: #ffffff;
  }
  * { margin: 0; padding: 0; box-sizing: border-box; }
  html, body {
    width: 1200px;
    height: 1029px;
    overflow: hidden;
    background: var(--paper);
  }
  .board {
    position: relative;
    width: 1200px;
    height: 1029px;
    background: var(--paper);
    font-family: "Archivo Narrow", "Arial Narrow", sans-serif;
  }

  /* Company name */
  .company-name {
    position: absolute;
    left: 0;
    top: 160px;
    width: 1200px;
    text-align: center;
    font-family: "Oswald", "Arial Narrow", sans-serif;
    font-weight: 700;
    font-size: 104px;
    line-height: 1;
    letter-spacing: 2px;
    color: var(--ink);
    text-transform: uppercase;
  }

  /* Mission / Vision banner */
  .statement-banner {
    position: absolute;
    left: 162px;
    top: 452px;
    width: 894px;
    height: 122px;
    background: var(--brand-red);
    overflow: hidden;
  }
  .statement-label {
    position: absolute;
    bottom: -4px;
    font-family: "Oswald", "Arial Narrow", sans-serif;
    font-weight: 500;
    font-size: 38px;
    line-height: 1;
    color: var(--white);
    transform: scaleX(0.72);
    transform-origin: left bottom;
    letter-spacing: -0.5px;
  }
  .statement-label.mission { left: 10px; }
  .statement-label.vision { left: 457px; }
  .statement-text {
    position: absolute;
    color: #ffe9c6;
    font-size: 19px;
    line-height: 24px;
  }
  .statement-text.mission { left: 97px; top: 5px; width: 350px; }
  .statement-text.vision { left: 538px; top: 16px; width: 350px; }

  /* Values panels */
  .value-panel {
    position: absolute;
    width: 525px;
    height: 122px;
    background: var(--panel-black);
    overflow: hidden;
  }
  .value-panel.col-left { left: 73px; }
  .value-panel.col-right { left: 621px; }
  .value-panel.row-1 { top: 588px; }
  .value-panel.row-2 { top: 732px; }
  .value-panel.row-3 { top: 877px; }

  .value-word {
    position: absolute;
    white-space: nowrap;
    font-size: 19px;
    line-height: 1;
    color: var(--value-gold);
  }
  .value-word.commitment  { left: 19px;  top: 6px; }
  .value-word.fairness    { left: 292px; top: 31px; }
  .value-word.ethical     { left: 129px; top: 40px; }
  .value-word.promise     { left: 204px; top: 62px; }
  .value-word.moral       { left: 97px;  top: 68px; }
  .value-word.right-thing { left: 286px; top: 94px; }
  .value-word.consistency { left: 144px; top: 99px; }
  .value-title {
    position: absolute;
    left: 9px;
    bottom: -4px;
    font-family: "Oswald", "Arial Narrow", sans-serif;
    font-weight: 500;
    font-size: 40px;
    line-height: 1;
    color: var(--white);
    transform: scaleX(0.68);
    transform-origin: left bottom;
    letter-spacing: -0.5px;
  }
</style>
</head>
<body>
<main class="board">
  <h1 class="company-name">Harlow Steelworks</h1>

  <section class="statement-banner">
    <p class="statement-text mission">To be the “Steel Fabricator of Choice” through innovative solutions and the consistent delivery of a high quality customer experience!</p>
    <h2 class="statement-label mission">MISSION</h2>
    <p class="statement-text vision">Exceptional People Fabricating Inspiring Projects</p>
    <h2 class="statement-label vision">VISION</h2>
  </section>

  <section class="value-panel col-left row-1">
    <span class="value-word commitment">Commitment</span>
    <span class="value-word fairness">Fairness</span>
    <span class="value-word ethical">Ethical</span>
    <span class="value-word promise">Do What We Say We Are Going to Do</span>
    <span class="value-word moral">Moral</span>
    <span class="value-word right-thing">Do the Right Thing Always</span>
    <span class="value-word consistency">Consistency</span>
    <h3 class="value-title">INTEGRITY</h3>
  </section>
  <section class="value-panel col-right row-1">
    <span class="value-word commitment">Commitment</span>
    <span class="value-word fairness">Fairness</span>
    <span class="value-word ethical">Ethical</span>
    <span class="value-word promise">Do What We Say We Are Going to Do</span>
    <span class="value-word moral">Moral</span>
    <span class="value-word right-thing">Do the Right Thing Always</span>
    <span class="value-word consistency">Consistency</span>
    <h3 class="value-title">INTEGRITY</h3>
  </section>

  <section class="value-panel col-left row-2">
    <span class="value-word commitment">Commitment</span>
    <span class="value-word fairness">Fairness</span>
    <span class="value-word ethical">Ethical</span>
    <span class="value-word promise">Do What We Say We Are Going to Do</span>
    <span class="value-word moral">Moral</span>
    <span class="value-word right-thing">Do the Right Thing Always</span>
    <span class="value-word consistency">Consistency</span>
    <h3 class="value-title">INTEGRITY</h3>
  </section>
  <section class="value-panel col-right row-2">
    <span class="value-word commitment">Commitment</span>
    <span class="value-word fairness">Fairness</span>
    <span class="value-word ethical">Ethical</span>
    <span class="value-word promise">Do What We Say We Are Going to Do</span>
    <span class="value-word moral">Moral</span>
    <span class="value-word right-thing">Do the Right Thing Always</span>
    <span class="value-word consistency">Consistency</span>
    <h3 class="value-title">INTEGRITY</h3>
  </section>

  <section class="value-panel col-left row-3">
    <span class="value-word commitment">Commitment</span>
    <span class="value-word fairness">Fairness</span>
    <span class="value-word ethical">Ethical</span>
    <span class="value-word promise">Do What We Say We Are Going to Do</span>
    <span class="value-word moral">Moral</span>
    <span class="value-word right-thing">Do the Right Thing Always</span>
    <span class="value-word consistency">Consistency</span>
    <h3 class="value-title">INTEGRITY</h3>
  </section>
  <section class="value-panel col-right row-3">
    <span class="value-word commitment">Commitment</span>
    <span class="value-word fairness">Fairness</span>
    <span class="value-word ethical">Ethical</span>
    <span class="value-word promise">Do What We Say We Are Going to Do</span>
    <span class="value-word moral">Moral</span>
    <span class="value-word right-thing">Do the Right Thing Always</span>
    <span class="value-word consistency">Consistency</span>
    <h3 class="value-title">INTEGRITY</h3>
  </section>
</main>
</body>
</html>
```